Brindle Structures Construction Company Seeking Modern Website

We are a small construction company wanting to create a web presence. We don't have much in the way of current content but will get photos as they come in. Attached is a picture of our business card.
The pages we would like on the menu are:
Home
Portfolio
Product Specs
Testimonials
Our Process
Contact
Some designs we like are:
http://www.tovenquarnsheds.example/
http://www.qzrsheds.example/
http://pannowsheds.example/
http://wistenhalls.example/
Not much requirements other than that so feel free to be creative!
Updates
Target Market(s)
Construction
Commercial and Residential Buildings
Industry/Entity Type
Construction Company
Number of Pages Required
5+ page
Look and feel

```html
<!DOCTYPE html>
<html lang="en">
<head>
<meta charset="utf-8">
<title>Brindle Structures</title>
<link href="https://fonts.googleapis.com/css2?family=Lato:ital,wght@0,400;0,700;0,900;1,400&family=Oswald:wght@400&family=Merienda:wght@400&family=Open+Sans:wght@400;600&display=swap" rel="stylesheet">
<style>
:root{
  --blue:#1aa0dc;
  --blue-deep:#2196c9;
  --dark:#2f2f2f;
  --red:#d7261e;
  --text:#555;
  --white:#fff;
}
*{box-sizing:border-box;margin:0;padding:0}
html,body{width:768px;height:1200px;overflow:hidden;background:var(--white);font-family:"Lato",sans-serif;color:var(--text)}
.page{position:relative;width:768px;height:1200px;overflow:hidden}
.abs{position:absolute}

.topbar{top:0;left:0;width:768px;height:24px;background:var(--blue)}
.lang{left:84px;top:4px;height:15px;width:48px;border:1px solid rgba(255,255,255,.5);color:#fff;font-size:9px;padding:1px 5px;line-height:12px}
.social{top:0;left:561px;display:flex}
.social span{width:24px;height:24px;border-left:1px solid rgba(255,255,255,.25);background:#1789bd;display:flex;align-items:center;justify-content:center}
.social i{display:block;width:9px;height:9px;background:rgba(255,255,255,.85)}

.header{top:24px;left:0;width:768px;height:60px;background:#fff}
.brand{left:84px;top:43px;font-weight:900;font-size:24px;color:var(--blue);display:flex;align-items:center;gap:8px}
.brand b{display:inline-block;width:18px;height:18px;border-radius:50%;background:var(--red)}
.call{right:84px;top:47px;font-size:13px;display:flex;align-items:center;gap:10px}
.call em{color:#666;font-style:italic}
.call a{color:var(--blue);text-decoration:none}

.nav{top:84px;left:0;width:768px;height:30px;background:var(--dark)}
.nav ul{position:absolute;left:84px;top:0;display:flex;list-style:none}
.nav li{width:100px;height:30px;line-height:30px;text-align:center;color:#fff;font-size:9.5px;border-right:1px solid #444;white-space:nowrap}
.nav li.active{background:var(--blue)}

.hero{top:114px;left:0;width:768px;height:218px;background:linear-gradient(180deg,#b5cde0 0%,#8aa9c1 70%,#a8cf62 88%,#9ccb56 100%)}
.hero-title{right:84px;top:168px;font-family:"Oswald",sans-serif;font-size:23px;line-height:30px;color:#fff;text-align:right;text-shadow:0 1px 2px rgba(0,0,0,.4)}

.welcome{top:332px;left:0;width:768px;height:112px;background:var(--blue);color:#fff;text-align:center}
.welcome h1{margin-top:13px;font-weight:400;font-size:19px;letter-spacing:.3px}
.welcome .rule{width:190px;height:1px;background:rgba(255,255,255,.7);margin:6px auto 0;position:relative}
.welcome .rule:after{content:"";position:absolute;left:86px;top:0;border:9px solid transparent;border-top:8px solid #fff;border-bottom:0}
.welcome p{width:600px;margin:11px auto 0;font-size:9.2px;line-height:13.5px}
.plus{left:368px;top:428px;width:32px;height:16px;background:var(--dark);color:#fff;font-size:15px;line-height:15px;text-align:center;border-radius:2px 2px 0 0}

.card{top:490px;width:185px;height:194px;background:#fff;border:1px solid #ddd;border-top:2px solid #333;box-shadow:0 6px 8px -6px rgba(0,0,0,.2);font-size:8px;line-height:12px}
.pill{position:absolute;left:32px;top:-14px;width:120px;height:28px;border-radius:50%;background:var(--red);border:2px solid #9c1b15;color:#fff;font-family:"Merienda",cursive;font-size:13px;text-align:center;line-height:24px}
.more{position:absolute;right:9px;color:var(--blue);font-size:7.5px;font-weight:700;letter-spacing:.2px}
.photo-team{position:absolute;left:7px;top:36px;width:170px;height:73px;background:linear-gradient(135deg,#a7bfcf,#d9a98d 50%,#bfd2dc);border:1px solid #999}
.about p{position:absolute;left:9px;top:118px;width:168px;color:#555}
.item{position:absolute;left:10px;width:170px}
.item h3{font-weight:700;font-size:10.2px;color:#333;margin-left:16px;line-height:14px}
.item p{margin-left:26px;color:#666}
.item svg{position:absolute;left:0;top:2px}
.sep{position:absolute;left:10px;width:170px;border-top:1px dashed #bbb}
.news{position:absolute;left:8px;width:170px;display:flex;gap:7px}
.date{width:24px;height:25px;border:1px solid #5aa9cf;border-radius:3px;text-align:center;font-size:10px;color:#555;flex:none;line-height:14px;overflow:hidden}
.date span{display:block;background:var(--blue);color:#fff;font-size:6.5px;line-height:9px}
.news h4{font-weight:400;font-size:8px;color:#333;line-height:11px}
.news p{font-size:7.5px;color:#666;line-height:11px}
.news-sep{position:absolute;left:8px;width:170px;border-top:1px dotted #bbb}

.types-line{top:748px;left:84px;width:600px;height:2px;background:#333}
.types{top:750px;left:0;width:768px;height:160px;background:var(--blue-deep)}
.types-pill{left:324px;top:735px;width:120px;height:28px;border-radius:50%;background:var(--red);border:2px solid #9c1b15;color:#fff;font-family:"Merienda",cursive;font-size:13px;text-align:center;line-height:24px;z-index:2}
.tile{top:780px;width:145px;height:102px;border:2px solid #e6e6e6;background:#ddd}
.tile .img{height:80px}
.tile .cap{height:18px;background:rgba(255,255,255,.85);text-align:center;font-family:"Open Sans",sans-serif;font-size:10px;line-height:18px;color:#333}
.arrow{top:825px;color:#e9e2c8;font-size:16px}

.say{top:942px;left:0;width:768px;text-align:center;font-family:"Open Sans",sans-serif}
.say h2{color:var(--red);font-weight:400;font-size:19px}
.say p{color:#555;font-size:15px;margin-top:2px}
.quote{top:1003px;left:84px;width:520px;height:64px;border:1px solid #ddd;box-shadow:0 2px 4px rgba(0,0,0,.12);background:#fff;padding:10px 12px;font-size:8.5px;line-height:15px;font-style:italic;color:#333;text-indent:28px}
.quote-tail{left:540px;top:1064px}
.avatar{left:598px;top:998px;width:76px;height:76px;border-radius:50%;background:radial-gradient(circle at 50% 40%,#cfd8df,#8ea5b5);border:4px solid #fff;box-shadow:0 1px 5px rgba(0,0,0,.3)}
.who{left:500px;top:1082px;font-size:8.5px;font-style:italic;font-weight:700;color:#333}

.footer{top:1123px;left:0;width:768px;height:73px;background:var(--dark)}
.footer ul{position:absolute;left:84px;top:28px;display:flex;list-style:none}
.footer li{font-size:7.8px;color:#fff;padding:0 8px;border-right:1px solid #555}
.footer li:first-child{padding-left:2px;color:var(--blue)}
.footer li:last-child{border:0}
.foot-brand{right:84px;top:1139px;display:flex;align-items:center;gap:4px}
.foot-brand .c{width:25px;height:25px;border-radius:50%;background:var(--blue);display:flex;align-items:center;justify-content:center}
.foot-brand .c.g{background:#666}
.foot-brand strong{font-weight:900;font-size:14px;color:#aaa;margin-left:6px}
.copy{right:84px;top:1178px;font-size:8px;color:#ddd}
.bottom-strip{top:1196px;left:0;width:768px;height:4px;background:var(--blue)}
</style>
</head>
<body>
<div class="page">
  <div class="abs topbar"></div>
  <div class="abs lang">English &#8964;</div>
  <div class="abs social">
    <span><svg width="10" height="10" viewBox="0 0 10 10"><circle cx="4" cy="4" r="3" fill="none" stroke="#fff" stroke-width="1.4"/><line x1="6.2" y1="6.2" x2="9" y2="9" stroke="#fff" stroke-width="1.5"/></svg></span>
    <span><i></i></span><span><i></i></span><span><i></i></span><span><i></i></span>
  </div>

  <div class="abs header"></div>
  <div class="abs brand"><b></b>Brindle Structures</div>
  <div class="abs call"><em>Call us TODAY !</em>
    <svg width="11" height="11" viewBox="0 0 12 12"><path d="M2 1l2.5 0 1 3-1.5 1c.8 1.6 2 2.8 3.5 3.5l1-1.5 3 1V11c-5 .5-10-4.5-9.5-10z" fill="#1aa0dc"/></svg>
    <a>+123 555 0182</a></div>

  <nav class="abs nav"><ul>
    <li class="active">HOME</li><li>PORTFOLIO</li><li>PRODUCT SPECS</li><li>TESTIMONIALS</li><li>OUR PROCESS</li><li>CONTACT US</li>
  </ul></nav>

  <div class="abs hero" role="img" aria-label="Illustration of colourful houses on green hills under a blue sky"></div>
  <div class="abs hero-title">BUILDING DREAMS,<br>SO YOU CAN BUILD MEMORIES</div>

  <section class="abs welcome">
    <h1>WELCOME TO BRINDLE STRUCTURES</h1>
    <div class="rule"></div>
    <p>Lorem ipsum dolor sit amet, consectetur adipiscing elit. Praesent volutpat ultricies euismod. Mauris consectetur tellus quis sem dictum pharetra. Nullam euismod nunc blandit mi sagittis, et posuere nunc iaculis. Aenean in sollicitudin quam, non accumsan ipsum. Vivamus in aliquet ex. Nullam malesuadammodo mi, tristique faucibus nisl condimentum condimentum. Duis porttitor nisi ut elementum so</p>
  </section>
  <div class="abs plus">+</div>

  <div class="abs card about" style="left:84px">
    <div class="pill">About Us</div>
    <div class="photo-team" role="img" aria-label="Photo of many hands stacked together"></div>
    <p>Hendrerit in vulputate molestie consquat, sisi atvero eros et accumsan iustoodio dignissimr qui blandit praesent luptatulenit auedolore te feugait nulla facilisilestie conseyat,</p>
    <div class="more" style="top:172px">READ MORE &#9679;</div>
  </div>

  <div class="abs card" style="left:292px">
    <div class="pill">What We Do</div>
    <div class="item" style="top:34px">
      <svg width="10" height="8" viewBox="0 0 10 8"><path d="M1 4l3 3 5-6" fill="none" stroke="#3a8f8a" stroke-width="2"/></svg>
      <h3>Vulputate Molestie Consequat</h3>
      <p>quis nostrud exsetiperj aliquip commod consequa uisquis nostru suscipit nisl roli aliquip exea commod</p>
    </div>
    <div class="more" style="top:92px">KNOW MORE</div>
    <div class="sep" style="top:108px"></div>
    <div class="item" style="top:117px">
      <svg width="10" height="8" viewBox="0 0 10 8"><path d="M1 4l3 3 5-6" fill="none" stroke="#3a8f8a" stroke-width="2"/></svg>
      <h3>Vulputate Molestie Consequat</h3>
      <p>quis nostrud exetiperj saliquip commodr consequa uisquis nostru iexetip suscipitt lobtis nisl ut aliquip exea commod</p>
    </div>
    <div class="more" style="top:174px">KNOW MORE</div>
  </div>

  <div class="abs card" style="left:500px">
    <div class="pill">Latest News</div>
    <div class="news" style="top:38px"><div class="date">25<span>NOV</span></div><div><h4>Vero eros accumsaet odio</h4><p>quis nostrud exetiperj suscipit lobtis nisl ut aliquip ex ea commod</p></div></div>
    <div class="news-sep" style="top:82px"></div>
    <div class="news" style="top:88px"><div class="date">22<span>NOV</span></div><div><h4>Eros accumsaet iusto odio</h4><p>quis nostrud exetiperj suscipit lobtfis nisl ut aliquip exea commod</p></div></div>
    <div class="news-sep" style="top:129px"></div>
    <div class="news" style="top:135px"><div class="date">20<span>NOV</span></div><div><h4>Croeros accumsaet iusto odio</h4><p>quis nostrud exetiperj suscipit lobtisf nisl ut aliquip ex commod</p></div></div>
    <div class="more" style="top:172px">READ MORE &#9679;</div>
  </div>

  <div class="abs types-line"></div>
  <div class="abs types"></div>
  <div class="abs types-pill">Building Types</div>
  <div class="abs arrow" style="left:68px">&#8249;</div>
  <div class="abs arrow" style="left:692px">&#8250;</div>
  <div class="abs tile" style="left:85px"><div class="img" role="img" aria-label="Photo of farm shop buildings" style="background:linear-gradient(180deg,#c9cccc 0%,#a9a49a 60%,#7f8a5e 100%)"></div><div class="cap">Farm Shops</div></div>
  <div class="abs tile" style="left:236px"><div class="img" role="img" aria-label="Photo of an open machine storage shed" style="background:linear-gradient(180deg,#9cc0e0 0%,#4d6a7e 45%,#6c7f5a 100%)"></div><div class="cap">Machine Storage</div></div>
  <div class="abs tile" style="left:387px"><div class="img" role="img" aria-label="Photo of a seed dealership with grain silos" style="background:linear-gradient(180deg,#7fb3e3 0%,#c9d3d0 45%,#6d8f48 100%)"></div><div class="cap">Seed Dealership</div></div>
  <div class="abs tile" style="left:538px"><div class="img" role="img" aria-label="Aerial photo of a long dairy barn" style="background:linear-gradient(180deg,#6f9a4c 0%,#c8c2a8 45%,#c49a43 100%)"></div><div class="cap">Dairy</div></div>

  <div class="abs say"><h2>What Our Customers Say</h2><p>Lorem ipsum dolor sit amet consectetur Donec a consequat mag</p></div>
  <div class="abs quote">Lorem sum dolor sit amet, consectetuer adipiscing elit, sed diam nonummy nibh euismod tincidunt ut laoreet re agn aliqam erat volutpat wisi enim ad minim veniam, quis nostrud exerci tation ullamcorper suscipit lobortis nisl ut aliquip modo conseuatis autem vel eum iriure dolor in hendrerit in vulputate velit esse molestie consequat, vel illum dolore eu.</div>
  <svg class="abs quote-tail" width="16" height="10" viewBox="0 0 16 10"><path d="M0 0l8 9 8-9" fill="#fff" stroke="#ddd"/><rect x="0" y="0" width="16" height="1.5" fill="#fff"/></svg>
  <div class="abs avatar" role="img" aria-label="Customer portrait photo"></div>
  <div class="abs who">Tomas, Northfield, USA</div>

  <footer class="abs footer">
    <ul><li>HOME</li><li>PORTFOLIO</li><li>PRODUCT SPACS</li><li>TESTIMONIALS</li><li>OUR PROCESS</li><li>CONTACT US</li></ul>
  </footer>
  <div class="abs foot-brand">
    <span class="c"><svg width="10" height="13" viewBox="0 0 10 13"><rect x="1" y="0.5" width="8" height="12" rx="1.5" fill="none" stroke="#fff" stroke-width="1.2"/><rect x="2.5" y="2" width="5" height="7" fill="#fff"/></svg></span>
    <span class="c g"><svg width="13" height="9" viewBox="0 0 13 9"><rect x="0.5" y="0.5" width="12" height="8" fill="none" stroke="#fff"/><path d="M.5 .5l6 4.5 6-4.5" fill="none" stroke="#fff"/></svg></span>
    <strong>Brindle Structures</strong>
  </div>
  <div class="abs copy">Copyright &copy; 2015 Brindle Structures &nbsp;| &nbsp;All Rights Reserved</div>
  <div class="abs bottom-strip"></div>
</div>
</body>
</html>
```